Label Redesign For Hemp Oil Tincture Bottle*

I need a label redesigned for Marbleleaf Hemp, current bottle label and logo is attached. The current label doesn't standout, not sure if its the font size or colors on the existing label. It is very important to have on the label that this is a Premium Full Spectrum Hemp Oil that is 2000mg. Then after the label is redesigned and approved, I would need to packaging to be designed to match the approved label design.
This Hemp oil has a relaxing effect to help ease mental and emotional stress, tension and worry. The Omega Fatty Acids it contains also naturally improves your mood and overall brain function, causing you to feel more alert and focused. Hemp Oil helps with insomnia. Take some 2-3 hours before bedtime, you will feel relaxed yet aware of how tired you are that it will lead to a good night's sleep. Hemp Oil helps ease chronic pain and inflammation from conditions such as arthritis, fibromyalgia, lupus, and MS. As a pain relief supplement, it is a safer, natural, non-chemical and non-addictive alternative to prescription painkillers.

Target Market(s)

Adults

Industry/Entity Type

Supplement

Font styles to use
Serif
Sans Serif

Colors

Designer to choose colors to be used in the design.

Requirements
Must have
• All information thats on current label but where it says 750 in the front of the existing label, it needs to say 2000. The 2000 should be prominent on the label.

```html
<!DOCTYPE html>
<html lang="en">
<head>
<meta charset="UTF-8">
<title>Marbleleaf Hemp – Hemp Oil Label</title>
<link href="https://fonts.googleapis.com/css2?family=Barlow:wght@400;500;600&family=Quicksand:wght@400&display=swap" rel="stylesheet">
<style>
  :root {
    --backdrop: #cdcdcd;
    --label-white: #ffffff;
    --label-shade: #c9d4dc;
    --green: #4a9a2c;
    --green-light: #6cb33f;
    --green-dark: #2f6e1c;
    --text-dark: #3a3a3a;
    --zero-green: #6cb33f;
  }
  * { margin: 0; padding: 0; box-sizing: border-box; }
  html, body {
    width: 1200px; height: 1200px; overflow: hidden;
    background: var(--backdrop);
  }
  .label {
    position: absolute;
    left: 250px; top: 60px;
    width: 700px; height: 1080px;
    background: linear-gradient(90deg, var(--label-shade) 0%, #e8edf0 35%, var(--label-white) 70%);
    font-family: "Barlow", sans-serif;
    text-align: center;
  }
  .top-strip {
    position: absolute; left: 0; top: 0; width: 100%; height: 27px;
    background: linear-gradient(90deg, var(--green), var(--green-light));
  }
  .brand {
    position: absolute; top: 72px; left: 0; width: 100%;
    display: flex; justify-content: center; align-items: center; gap: 22px;
  }
  .brand-dot {
    width: 70px; height: 70px; border-radius: 50%;
    background: var(--green);
  }
  .brand-text { text-align: center; line-height: 1.15; }
  .brand-name {
    font-size: 34px; font-weight: 500; color: var(--text-dark);
    letter-spacing: 1px; text-transform: uppercase;
  }
  .brand-tag {
    font-size: 32px; font-weight: 400; color: var(--zero-green);
    letter-spacing: 1px;
  }
  .strength-band {
    position: absolute; top: 232px; left: 0; width: 100%; height: 150px;
    background: linear-gradient(90deg, var(--green-dark), var(--green) 50%, var(--green-light));
    color: var(--label-white);
    padding-top: 10px;
  }
  .strength-kicker { font-size: 42px; font-weight: 400; line-height: 1.1; }
  .strength-amount {
    font-family: "Quicksand", sans-serif;
    font-size: 88px; font-weight: 400; letter-spacing: 14px; line-height: 1;
  }
  .drop-art {
    position: absolute; top: 432px; left: 241px; width: 218px; height: 330px;
    border-radius: 12px;
    background: linear-gradient(135deg, var(--green-light), var(--green) 50%, var(--green-dark));
  }
  .product-name {
    position: absolute; top: 800px; left: 0; width: 100%;
    font-size: 120px; font-weight: 600; color: var(--green);
    line-height: 1;
  }
  .info-band {
    position: absolute; top: 918px; left: 0; width: 100%; height: 98px;
    background: linear-gradient(90deg, var(--green-dark), var(--green) 50%, var(--green-light));
    color: var(--label-white);
    padding-top: 12px;
  }
  .info-type { font-size: 36px; font-weight: 500; letter-spacing: 7px; line-height: 1.1; }
  .info-flavor { font-size: 33px; font-weight: 400; line-height: 1.1; }
  .volume {
    position: absolute; top: 1036px; left: 0; width: 100%;
    font-size: 30px; font-weight: 600; color: var(--text-dark);
  }
</style>
</head>
<body>
  <main class="label">
    <div class="top-strip"></div>

    <header class="brand">
      <div class="brand-dot"></div>
      <div class="brand-text">
        <div class="brand-name">Marbleleaf<br>Hemp</div>
        <div class="brand-tag">ZERO THC</div>
      </div>
    </header>

    <section class="strength-band">
      <div class="strength-kicker">PREMIUM FULL SPECTRUM</div>
      <div class="strength-amount">2000MG</div>
    </section>

    <div class="drop-art" role="img" aria-label="Green faceted oil drop illustration"></div>

    <h1 class="product-name">HEMP OIL</h1>

    <section class="info-band">
      <div class="info-type">DIETARY SUPPLIMENT</div>
      <div class="info-flavor">NATURAL PEPPERMINT FLAVOR</div>
    </section>

    <div class="volume">1FL.OZ (30ML)</div>
  </main>
</body>
</html>
```